Brivora Collective Business Card Design

We need a business card design for Brivora Collective. We are a healthcare recruiting, wellness and education company. We partner with medical facilities to find quality candidates. We also offer free wellness courses.
The final design should communicate an emphasis on recruiting and wellness
The main purpose of the business card is to utilized it for networking events, give to hospitals, executives, VCs surgery centers and clinics. I want it to be sleek, clean, use of our brand colors and professional.

```html
<!DOCTYPE html>
<html lang="en">
<head>
<meta charset="utf-8">
<title>Brivora Collective — Business Card</title>
<link rel="stylesheet" href="https://fonts.googleapis.com/css2?family=Arimo:wght@400&family=Oswald:wght@600&display=swap">
<style>
  :root {
    --backdrop: #d9d9d6;
    --card: #1f1f20;
    --card-deep: #121213;
    --pattern-light: #3a3a3c;
    --teal: #0e6b60;
    --white: #f2f2f2;
    --muted: #6b6b6b;
  }
  * { margin: 0; padding: 0; box-sizing: border-box; }
  html, body {
    width: 1200px; height: 912px; overflow: hidden;
    background: var(--backdrop);
    font-family: "Arimo", Arial, sans-serif;
  }
  .sheet {
    width: 1200px; height: 912px;
    display: flex; flex-direction: column;
    align-items: center; justify-content: center; gap: 40px;
  }
  .card {
    position: relative;
    width: 700px; height: 400px;
    background: var(--card);
    overflow: hidden;
    box-shadow: 0 6px 18px rgba(0,0,0,.18);
  }
  .card::after {
    content: ""; position: absolute; left: 0; right: 0; bottom: 0;
    height: 7px; background: var(--teal);
  }
  /* front */
  .card-front .pattern-field {
    position: absolute; inset: 0 0 7px 0;
    background: linear-gradient(180deg, var(--pattern-light) 0%, var(--card) 45%, var(--card-deep) 100%);
  }
  .card-front .brand-mark {
    position: absolute; left: 50%; top: 42%;
    transform: translate(-50%, -50%);
    display: flex; align-items: center; gap: 10px;
    color: var(--teal); font-size: 30px; white-space: nowrap;
  }
  .brand-square { width: 18px; height: 18px; background: var(--teal); }
  /* back */
  .card-back .brand-mark {
    position: absolute; left: 50%; top: 62px;
    transform: translateX(-50%);
    display: flex; align-items: center; gap: 12px;
    color: var(--teal); font-size: 36px; white-space: nowrap;
  }
  .card-back .brand-square { width: 22px; height: 22px; }
  .identity {
    position: absolute; right: 385px; top: 170px;
    text-align: right;
  }
  .person-name {
    font-family: "Oswald", "Arial Narrow", sans-serif;
    font-weight: 600; font-size: 38px; letter-spacing: .5px;
    color: var(--teal); text-transform: uppercase; line-height: 1.05;
  }
  .person-role { color: var(--white); font-size: 19px; margin-top: 4px; }
  .divider {
    position: absolute; left: 335px; top: 160px;
    width: 1px; height: 90px; background: var(--muted);
  }
  .contact-list {
    position: absolute; left: 356px; top: 164px;
    list-style: none; color: var(--white); font-size: 17px;
  }
  .contact-list li { display: flex; align-items: center; gap: 9px; height: 27px; }
  .contact-list svg { width: 13px; height: 13px; fill: none; stroke: var(--teal); stroke-width: 2; }
  .address {
    position: absolute; left: 0; right: 0; top: 300px;
    text-align: center; color: var(--white); font-size: 19px;
  }
</style>
</head>
<body>
<main class="sheet">
  <section class="card card-front" aria-label="Card front">
    <div class="pattern-field" role="img" aria-label="Glossy black pattern of scattered angular tiles fading from grey to black"></div>
    <div class="brand-mark"><span class="brand-square"></span><span>Brivora Collective</span></div>
  </section>

  <section class="card card-back" aria-label="Card back">
    <div class="brand-mark"><span class="brand-square"></span><span>Brivora Collective</span></div>

    <div class="identity">
      <div class="person-name">Marcus Ellery</div>
      <div class="person-role">Director</div>
    </div>

    <div class="divider"></div>

    <ul class="contact-list">
      <li>
        <svg viewBox="0 0 14 14"><path d="M3 1.5l2 2.5-1.2 1.4a8 8 0 0 0 4.8 4.8L10 9l2.5 2-1 2C6 13 1 8 1 2.5z"/></svg>
        555-014-2290
      </li>
      <li>
        <svg viewBox="0 0 14 14"><rect x="1" y="3" width="12" height="8"/><path d="M1 3l6 5 6-5"/></svg>
        info@brivoracollective.com
      </li>
      <li>
        <svg viewBox="0 0 14 14"><circle cx="7" cy="7" r="6"/><path d="M1 7h12M7 1c-3 3.5-3 8.5 0 12M7 1c3 3.5 3 8.5 0 12"/></svg>
        www.brivoracollective.com
      </li>
    </ul>

    <p class="address">2170 Larkmoor Pkwy Fairhaven, GA 30199</p>
  </section>
</main>
</body>
</html>
```